Cybersecurity company is looking for business card.

I need a business card design for our company, we are a cybersecurity company providing advance technology to protect agains any kind of malware. We need a fresh modern design it should communicate modern, technology and growth.

Target Market(s)

Business to business

Industry/Entity Type

Business

Contact Information for Business Card

Should have location, address, fax, mobile, phone, email and website.

Requirements
Must have
• Must follow company's logo color and style. Must have the company's log on its.

```html
<!DOCTYPE html>
<html lang="en">
<head>
<meta charset="utf-8">
<title>veltrix business card</title>
<link rel="stylesheet" href="https://fonts.googleapis.com/css2?family=Open+Sans:wght@400;600;700&display=swap">
<style>
  :root {
    --backdrop: #a9a4a6;
    --card-dark: #050505;
    --card-light: #ffffff;
    --ink: #1a1a1a;
    --accent: #a8262b;
    --reverse: #ffffff;
  }
  * { margin: 0; padding: 0; box-sizing: border-box; }
  html, body {
    width: 1200px;
    height: 801px;
    overflow: hidden;
    background: var(--backdrop);
    font-family: "Open Sans", Arial, sans-serif;
  }
  .canvas {
    position: relative;
    width: 1200px;
    height: 801px;
  }
  .card {
    position: absolute;
    box-shadow: 0 2px 6px rgba(0,0,0,0.25);
  }
  .card-front {
    left: 128px;
    top: 250px;
    width: 525px;
    height: 300px;
    background: var(--card-dark);
    display: flex;
    align-items: center;
    justify-content: center;
  }
  .wordmark {
    display: flex;
    align-items: center;
    gap: 12px;
    font-weight: 700;
    letter-spacing: 1px;
    text-transform: lowercase;
  }
  .wordmark-dot {
    width: 12px;
    height: 12px;
    border-radius: 50%;
    background: var(--accent);
  }
  .card-front .wordmark {
    color: var(--reverse);
    font-size: 60px;
  }
  .card-back {
    left: 773px;
    top: 138px;
    width: 300px;
    height: 525px;
    background: var(--card-light);
    color: var(--ink);
    display: flex;
    flex-direction: column;
    align-items: center;
    padding-top: 44px;
    text-align: center;
  }
  .card-back .wordmark {
    color: var(--ink);
    font-size: 34px;
    gap: 8px;
  }
  .card-back .wordmark-dot {
    width: 8px;
    height: 8px;
  }
  .info-block {
    margin-top: 34px;
    display: flex;
    flex-direction: column;
    align-items: center;
    font-size: 14px;
    line-height: 1.35;
  }
  .info-block:first-of-type { margin-top: 40px; }
  .info-icon {
    width: 22px;
    height: 22px;
    margin-bottom: 8px;
    fill: var(--accent);
  }
  .website { font-weight: 700; }
</style>
</head>
<body>
<main class="canvas">
  <section class="card card-front" aria-label="Card front">
    <div class="wordmark"><span class="wordmark-dot"></span>veltrix</div>
  </section>

  <section class="card card-back" aria-label="Card back">
    <div class="wordmark"><span class="wordmark-dot"></span>veltrix</div>

    <div class="info-block address">
      <svg class="info-icon" viewBox="0 0 24 24" aria-hidden="true">
        <path d="M12 1.5c-4.4 0-7.8 3.4-7.8 7.6 0 5.6 7.8 13.4 7.8 13.4s7.8-7.8 7.8-13.4c0-4.2-3.4-7.6-7.8-7.6zm0 10.6a3 3 0 1 1 0-6 3 3 0 0 1 0 6z"/>
      </svg>
      <p>Dubai - UAE</p>
      <p>Harbor Tech Park (HTP)</p>
      <p>- Coral Bay Avenue</p>
    </div>

    <div class="info-block phones">
      <svg class="info-icon" viewBox="0 0 24 24" aria-hidden="true">
        <path d="M6.6 10.8c1.4 2.8 3.8 5.2 6.6 6.6l2.2-2.2c.3-.3.7-.4 1-.2 1.1.4 2.3.6 3.6.6.6 0 1 .4 1 1V20c0 .6-.4 1-1 1C10.6 21 3 13.4 3 4c0-.6.4-1 1-1h3.5c.6 0 1 .4 1 1 0 1.3.2 2.5.6 3.6.1.3 0 .7-.2 1l-2.3 2.2z"/>
      </svg>
      <p>mobile: +000 55 010 2040</p>
      <p>phone: 00 010 2041</p>
      <p>fax: 00 010 2042</p>
    </div>

    <div class="info-block online">
      <svg class="info-icon" viewBox="0 0 24 24" aria-hidden="true">
        <path d="M2 5h20v14H2z M2 5l10 8 10-8" fill="var(--accent)" stroke="#ffffff" stroke-width="1.4" stroke-linejoin="round"/>
      </svg>
      <p>name.surname@veltrix.com</p>
      <p class="website">www.veltrix.com</p>
    </div>
  </section>
</main>
</body>
</html>
```